I needed some business cards done for my band. We are a 9 piece funk/horn band that plays a lot of private parties, wedding receptions and music festivals. We'd like a design with vivid colors that incorporates our logo. You can check out our website at www.brasslanternband.example to see what type of vibe we are going for.

```html
<!DOCTYPE html>
<html lang="en">
<head>
<meta charset="utf-8">
<title>Brass Lantern — Business Cards</title>
<link rel="stylesheet" href="https://fonts.googleapis.com/css2?family=Bungee&family=Source+Serif+4:wght@600;700&display=swap">
<style>
  :root {
    --backdrop: #acacac;
    --card-purple: #420d5f;
    --card-deep: #2c0844;
    --lime: #c6d927;
    --white: #ffffff;
    --stage-magenta: #a21bb8;
    --stage-violet: #5a1dc9;
  }
  * { margin: 0; padding: 0; box-sizing: border-box; }
  html, body { width: 1200px; height: 1000px; overflow: hidden; }
  body { background: var(--backdrop); position: relative; font-family: "Source Serif 4", Georgia, serif; }

  .card {
    position: absolute;
    left: 294px;
    width: 613px;
    height: 352px;
    background: var(--card-purple);
    overflow: hidden;
  }
  .card--front { top: 127px; }
  .card--back { top: 529px; }

  /* Front */
  .front-name {
    position: absolute;
    left: 40px;
    top: 70px;
    width: 360px;
    font-family: "Source Serif 4", Georgia, serif;
    font-weight: 700;
    font-size: 92px;
    line-height: 0.98;
    color: var(--lime);
  }
  .stage-photo {
    position: absolute;
    right: 0;
    top: 0;
    width: 250px;
    height: 352px;
    background:
      radial-gradient(circle at 30% 20%, rgba(140, 120, 255, 0.75), transparent 45%),
      radial-gradient(ellipse at 65% 60%, var(--stage-magenta), transparent 70%),
      linear-gradient(160deg, var(--stage-violet), var(--card-deep) 85%);
    -webkit-mask-image: linear-gradient(90deg, transparent 0, #000 70px);
            mask-image: linear-gradient(90deg, transparent 0, #000 70px);
  }

  /* Back */
  .faint-ring {
    position: absolute;
    left: 385px;
    top: 76px;
    width: 260px;
    height: 260px;
    border-radius: 50%;
    border: 16px solid rgba(44, 8, 68, 0.55);
  }
  .tagline {
    position: absolute;
    left: 60px;
    top: 62px;
    width: 400px;
    text-align: center;
    font-family: "Bungee", Impact, sans-serif;
    font-size: 30px;
    line-height: 38px;
    color: var(--white);
    letter-spacing: 0.5px;
    text-shadow: 2px 2px 0 #2a0540;
  }
  .band-name {
    position: absolute;
    left: 60px;
    top: 150px;
    font-family: "Source Serif 4", Georgia, serif;
    font-weight: 700;
    font-size: 62px;
    line-height: 1;
    color: var(--lime);
  }
  .contact {
    position: absolute;
    left: 60px;
    top: 248px;
    width: 420px;
    color: var(--white);
    font-weight: 600;
    font-size: 16px;
  }
  .contact-row {
    display: flex;
    justify-content: center;
    gap: 12px;
    line-height: 30px;
  }
  .contact-item { display: inline-flex; align-items: center; gap: 6px; white-space: nowrap; }
  .contact-item svg { width: 13px; height: 13px; fill: var(--lime); }
</style>
</head>
<body>

<section class="card card--front">
  <div class="front-name">Brass Lantern</div>
  <div class="stage-photo" role="img" aria-label="Photo of the band's singer performing at a microphone under purple stage lights"></div>
</section>

<section class="card card--back">
  <div class="faint-ring"></div>
  <p class="tagline">Where the soul<br>meets the groove</p>
  <div class="band-name">Brass Lantern</div>
  <div class="contact">
    <div class="contact-row">
      <span class="contact-item">
        <svg viewBox="0 0 16 16" aria-hidden="true"><path d="M3.5 1l2.5 3-1.5 2c1 2 3 4 5 5l2-1.5 3 2.5-1.5 2.5C7 15 1 9 1 2.5z"/></svg>
        555.014.2290
      </span>
      <span class="contact-item">
        <svg viewBox="0 0 16 16" aria-hidden="true"><path d="M1 3h14v10H1z M2 4l6 5 6-5" fill="none" stroke="#c6d927" stroke-width="1.6"/></svg>
        info@brasslanternband.example
      </span>
    </div>
    <div class="contact-row">
      <span class="contact-item">
        <svg viewBox="0 0 16 16" aria-hidden="true"><g fill="none" stroke="#c6d927" stroke-width="1.4"><circle cx="8" cy="8" r="6.5"/><ellipse cx="8" cy="8" rx="3" ry="6.5"/><path d="M1.5 8h13M2.5 4.5h11M2.5 11.5h11"/></g></svg>
        brasslanternband.example
      </span>
    </div>
  </div>
</section>

</body>
</html>
```